Velmar Industrial Coatings

We are looking to improve our business cards. Our company installs industrial floor and wall coatings in industrial, chemical and food processing plants.
Our coatings which consist of epoxy, urethane, and vinyl esters provide chemical and abrasion resistant surface with non-skid properties that are easy to clean.

Target Market(s)

food manufacturing, chemical plants, breweries and wineries, warehouses, clean room floors.

Industry/Entity Type

Construction

Contact Information for Business Card

improved current logo.

Colors

Designer to choose colors to be used in the design.

Requirements
Must have
• the information from uploaded file
Nice to have
• "We'll be outstanding on your floors."

```html
<!DOCTYPE html>
<html lang="en">
<head>
<meta charset="utf-8">
<title>Velmar Industrial Coatings – Business Card</title>
<link rel="stylesheet" href="https://fonts.googleapis.com/css2?family=Oswald:wght@500&family=Roboto:ital,wght@0,400;1,400&display=swap">
<style>
  :root {
    --backdrop: #e8e3e3;
    --card-dark: #231f20;
    --card-light: #fbfbfb;
    --ink: #222222;
    --ink-light: #ffffff;
    --accent: #2f4424;
  }
  * { margin: 0; padding: 0; box-sizing: border-box; }
  html, body {
    width: 1200px; height: 1200px; overflow: hidden;
    background: var(--backdrop);
  }
  .canvas { position: relative; width: 1200px; height: 1200px; }

  .card {
    position: absolute; left: 275px; width: 650px; height: 371px;
  }

  /* Front side */
  .card--front { top: 182px; background: var(--card-dark); color: var(--ink-light); }
  .front__name {
    position: absolute; left: 0; right: 0; top: 150px;
    text-align: center;
    font-family: "Oswald", sans-serif; font-weight: 500;
    font-size: 44px; letter-spacing: -0.5px; line-height: 1;
    transform: scaleX(0.86);
  }
  .front__web {
    position: absolute; left: 0; right: 0; top: 318px;
    text-align: center;
    font-family: "Roboto", sans-serif; font-style: italic;
    font-size: 25px; line-height: 1;
  }

  /* Back side */
  .card--back { top: 647px; background: var(--card-light); color: var(--ink); }
  .brand {
    position: absolute; left: 32px; top: 36px;
    display: flex; align-items: center; gap: 14px;
  }
  .brand__square { width: 52px; height: 52px; background: var(--accent); }
  .brand__name {
    font-family: "Oswald", sans-serif; font-weight: 500;
    font-size: 22px; color: var(--ink); letter-spacing: -0.2px;
  }

  .contacts {
    position: absolute; left: 32px; top: 240px;
    list-style: none;
    font-family: "Roboto", sans-serif; font-size: 18.5px; line-height: 26px;
  }
  .contacts li { display: flex; align-items: center; gap: 9px; }
  .contacts svg { width: 18px; height: 18px; fill: var(--accent); flex: none; }

  .person {
    position: absolute; right: 35px; top: 238px;
    text-align: right; font-family: "Roboto", sans-serif;
  }
  .person__name { font-size: 31px; line-height: 34px; color: var(--accent); }
  .person__tollfree { font-size: 22px; line-height: 24px; }
  .person__company, .person__address {
    font-size: 18px; line-height: 21px; padding-right: 5px;
  }
  .person__company { margin-top: 3px; }
</style>
</head>
<body>
<main class="canvas">
  <section class="card card--front">
    <h1 class="front__name">VELMAR INDUSTRIAL COATINGS INC.</h1>
    <p class="front__web">www.Velmarfloors.com</p>
  </section>

  <section class="card card--back">
    <div class="brand">
      <span class="brand__square"></span>
      <span class="brand__name">VELMAR INDUSTRIAL COATINGS INC.</span>
    </div>

    <ul class="contacts">
      <li>
        <svg viewBox="0 0 24 24" aria-hidden="true"><path d="M6.6 10.8a15.1 15.1 0 0 0 6.6 6.6l2.2-2.2c.3-.3.7-.4 1-.2 1.1.4 2.3.6 3.6.6.6 0 1 .4 1 1V20c0 .6-.4 1-1 1A17 17 0 0 1 3 4c0-.6.4-1 1-1h3.5c.6 0 1 .4 1 1 0 1.3.2 2.5.6 3.6.1.3 0 .7-.2 1z"/></svg>
        (360) 555-0131
      </li>
      <li>
        <svg viewBox="0 0 24 24" aria-hidden="true"><path d="M7 1h10a2 2 0 0 1 2 2v18a2 2 0 0 1-2 2H7a2 2 0 0 1-2-2V3a2 2 0 0 1 2-2zm0 3v15h10V4zm5 16.2a.9.9 0 1 0 0 1.8.9.9 0 0 0 0-1.8z"/></svg>
        (360) 555-0133
      </li>
      <li>
        <svg viewBox="0 0 24 24" aria-hidden="true"><path d="M6 2h9l3 3v4h2a2 2 0 0 1 2 2v10a2 2 0 0 1-2 2H4a2 2 0 0 1-2-2V11a2 2 0 0 1 2-2h2zm2 2v5h8V6h-2V4zm4 8v2h2v-2zm4 0v2h2v-2zm-4 4v2h2v-2zm4 0v2h2v-2z"/></svg>
        (360) 555-0117
      </li>
      <li>
        <svg viewBox="0 0 24 24" aria-hidden="true"><path d="M2 5h20v14H2zm2 2v.5l8 5.5 8-5.5V7zm0 3v7h16v-7l-8 5.5z"/></svg>
        neil@velmarfloors.com
      </li>
    </ul>

    <div class="person">
      <p class="person__name">NEIL CARVER</p>
      <p class="person__tollfree">1-800-555-0197</p>
      <p class="person__company">Velmar Inc.</p>
      <p class="person__address">PO Box 42, Fairhill, WA 98000</p>
    </div>
  </section>
</main>
</body>
</html>
```